Web site for small printshop

I am looking for a website for small printshop in Iceland, mainly serving university students and artist.

We print posters, flyers, business cards and more.

In addition to our current website, I would like to include design tool, (fx. www.quarlitune.example, www.dravonpix.example or something similar) jobs upload, shopping chart.
Updates

Great work, I am really amazed of the quality of work i am seeing here.

Really way beyond my expectation

GOOD JOB - all of you ! 

Hi all.

The designs submitted have been great, way better than expected.
I really did not expect this level of quality.

Some have been asking me for feedback on their designs, and I will try 
to send some feedback here, without spoiling your creativity.

Likes:
- when the colors of my logo is used in menus, buttons etc.
- simple, not to crowded look.

Dislikes.
- Dark and heavy design
- Lot of text and buttons (crowded look)

Extra info.
- top line (before menus) will contain: Tel - email - language
- menu line will have 5 categories: Home - service - submission of works - FAQ - about us
- 3 large buttons:  Job submit - Job design - ask for offer

LOVE YOUR WORK - great designs so far :)

Target Market(s)

University Students, Artists. Age group 20-30

Industry/Entity Type

University

Requirements
Must have
• The website must be easy to use, clean looking.

```html
<!DOCTYPE html>
<html lang="en">
<head>
<meta charset="utf-8">
<title>Hraunprent</title>
<link href="https://fonts.googleapis.com/css2?family=Open+Sans:wght@400;700;800&family=Arimo:wght@400;700&display=swap" rel="stylesheet">
<style>
:root{
  --red:#d9534a;
  --red-dark:#c4443b;
  --yellow:#f8d33c;
  --ink:#231b0c;
  --nav:#1e1e1e;
  --page:#efefef;
  --card:#f2f2f2;
  --text:#2e2e2e;
  --footer:#4a4a4a;
}
*{margin:0;padding:0;box-sizing:border-box}
html,body{width:1200px;height:1141px;overflow:hidden;background:#fff}
body{position:relative;font-family:"Arimo",Arial,sans-serif;color:var(--text)}
.top-band{position:absolute;left:0;top:0;width:1200px;height:521px;background:linear-gradient(#f4f4f4,#e9e9e9);border-bottom:2px solid #d6d6d6}
.brand{position:absolute;left:147px;top:17px;display:flex;align-items:center;gap:14px}
.brand-square{width:55px;height:73px;background:var(--red)}
.brand-name{font-family:"Open Sans",sans-serif;font-weight:700;font-size:44px;color:var(--ink);letter-spacing:.5px}
.nav-divider{position:absolute;left:585px;top:42px;width:1px;height:34px;background:#cfcfcf}
.nav a{position:absolute;top:50px;font-family:"Open Sans",sans-serif;font-weight:700;font-size:17px;color:var(--nav);text-decoration:none}
.hero{position:absolute;left:147px;top:103px;width:926px;height:364px;border-radius:0 14px 0 0;overflow:hidden}
.hero-scene{position:absolute;inset:0;background:linear-gradient(#d4e3ee 0%,#eaf1f5 45%,#dfe8e4 80%,#8fc040 88%,#6aa42a 100%)}
.hero-col{position:absolute;top:0;height:364px;background:rgba(235,235,235,.55)}
.col-a{left:0;width:297px}
.col-b{left:297px;width:314px;background:rgba(225,225,225,.45);border-left:1px solid rgba(255,255,255,.6);border-right:1px solid rgba(255,255,255,.6)}
.col-c{left:611px;width:315px;background:rgba(240,240,240,.3)}
.step-title{position:absolute;width:300px;text-align:center;font-family:"Arimo",sans-serif;font-weight:700;font-size:18px;letter-spacing:.6px;color:#1d1d1d}
.step-icon{position:absolute;width:84px;height:84px;border-radius:50%;background:var(--red);box-shadow:0 1px 3px rgba(0,0,0,.25)}
.step-icon::after{content:"";position:absolute;inset:5px;border:1.5px dashed rgba(255,255,255,.85);border-radius:50%}
.step-icon svg{position:absolute;left:20px;top:20px;width:44px;height:44px}
.joiner{position:absolute;width:52px;height:52px;border-radius:50%;background:var(--yellow);display:flex;align-items:center;justify-content:center;font-weight:700;font-size:21px;color:#222}
.laptop{position:absolute;left:60px;top:184px;width:205px;height:128px;background:linear-gradient(var(--red) 88%,#c9c9c9 88%);border:6px solid #2b2b2b;border-bottom:none;border-radius:6px 6px 0 0}
.run-btn{position:absolute;left:354px;top:219px;width:205px;height:51px;background:var(--red);color:#fff;font-weight:700;font-size:19px;letter-spacing:.5px;display:flex;align-items:center;justify-content:center;box-shadow:0 2px 2px rgba(0,0,0,.15)}
.print-art{position:absolute;left:680px;top:190px;width:171px;height:97px}
.print-art .back{position:absolute;left:0;top:25px;width:50px;height:62px;background:var(--red)}
.print-art .front{position:absolute;left:45px;top:0;width:126px;height:97px;background:var(--yellow)}
.print-art .front::after{content:"";position:absolute;inset:6px;border:1px dashed rgba(255,255,255,.9)}
.product-photo{position:absolute;top:554px;height:226px}
.feature{position:absolute;top:805px;height:245px;background:var(--card);padding:19px 19px 0 19px;font-size:16.6px;line-height:20.5px;text-align:justify}
.feature p+p{margin-top:21px}
.footer{position:absolute;left:0;top:1070px;width:1200px;height:71px;background:var(--footer);border-top:6px solid #d8d8d8}
.footer p{position:absolute;left:149px;top:34px;font-family:"Open Sans",sans-serif;font-size:11px;color:#fff}
</style>
</head>
<body>
<div class="top-band"></div>

<header>
  <div class="brand"><span class="brand-square"></span><span class="brand-name">HRAUNPRENT</span></div>
  <span class="nav-divider"></span>
  <nav class="nav">
    <a href="#" style="left:603px">HOME</a>
    <a href="#" style="left:681px">EDITOR</a>
    <a href="#" style="left:773px">CONTACT</a>
    <a href="#" style="left:878px">FAQ</a>
    <a href="#" style="left:936px">SUPPORT</a>
  </nav>
</header>

<section class="hero">
  <div class="hero-scene" role="img" aria-label="Sky with clouds over green grass, held as a printed sheet"></div>
  <div class="hero-col col-a"></div>
  <div class="hero-col col-b"></div>
  <div class="hero-col col-c"></div>

  <h2 class="step-title" style="left:-6px;top:40px">UPLOAD FILE</h2>
  <h2 class="step-title" style="left:305px;top:42px">CREATE NOW</h2>
  <h2 class="step-title" style="left:613px;top:43px">GET YOUR PRINT</h2>

  <div class="step-icon" style="left:103px;top:69px">
    <svg viewBox="0 0 44 44" fill="none" stroke="#fff" stroke-width="2.5"><path d="M14 6h16v16h8L22 38 6 22h8z"/></svg>
  </div>
  <div class="step-icon" style="left:414px;top:69px">
    <svg viewBox="0 0 44 44" fill="none" stroke="#fff" stroke-width="2.5"><path d="M14 10h16v14l-4 4v6h-8v-6l-4-4z"/><path d="M18 38h8M22 2v4M6 18h4M34 18h4M9 7l3 3M35 7l-3 3"/></svg>
  </div>
  <div class="step-icon" style="left:749px;top:69px">
    <svg viewBox="0 0 44 44" fill="none" stroke="#fff" stroke-width="2.5"><path d="M22 6l12 6v12l-12 6-12-6V12z"/><path d="M10 12l12 6 12-6M22 18v12M4 22l8 14h6M40 22l-8 14h-6"/></svg>
  </div>

  <div class="joiner" style="left:270px;top:88px">or</div>
  <div class="joiner" style="left:586px;top:88px">
    <svg width="20" height="18" viewBox="0 0 20 18"><path d="M2 1l17 8-17 8 4-8z" fill="#111"/></svg>
  </div>

  <div class="laptop" role="img" aria-label="Laptop showing a page layout"></div>

  <h2 class="step-title" style="left:305px;top:186px">USING OUR EDITOR</h2>
  <a class="run-btn">RUN EDITOR</a>

  <div class="print-art" role="img" aria-label="Printed yellow card with flower motif">
    <span class="back"></span><span class="front"></span>
  </div>
</section>

<div class="product-photo" role="img" aria-label="Red and white business cards" style="left:150px;width:289px;background:linear-gradient(135deg,#f1f1f1,#dcdcdc)"></div>
<div class="product-photo" role="img" aria-label="White t-shirt with printed lightbulb icon" style="left:461px;width:287px;background:linear-gradient(#ededed,#dfe2e6)"></div>
<div class="product-photo" role="img" aria-label="Red branded stationery set" style="left:767px;width:288px;background:linear-gradient(135deg,#e9e9e9,#b22a33 60%,#e3e3e3)"></div>

<article class="feature" style="left:149px;width:289px">
  <p>PressKit has been designed to be extensible via loading external modules to add unique functionalities.</p>
  <p>These modules are compiled assets designed and maintained outside of the main application. Current modules are Camera and QR Code generator.</p>
</article>
<article class="feature" style="left:460px;width:289px">
  <p>PressKit has been designed to be extensible via loading external modules to add unique functionalities.</p>
  <p>These modules are compiled assets designed and maintained outside of the main application. Current modules are Camera and QR Code generator.</p>
</article>
<article class="feature" style="left:766px;width:289px">
  <p>PressKit has been designed to be extensible via loading external modules to add unique functionalities.</p>
  <p>These modules are compiled assets designed and maintained outside of the main application. Current modules are Camera and QR Code generator.</p>
</article>

<footer class="footer"><p>All Content Copyright 2012 - HRAUNPRENT. All Rights Reserved.</p></footer>
</body>
</html>
```